2 Page Business Flyer for Finance Business

Need a two page flyer created for a finance business. Lots of text and needs to fit on two pages.

Corporate business/banking look and feel. Not too many large images. Lots of white space, clean design. Attached is color palette and the text contents of the flyer.

```html
<!DOCTYPE html>
<html lang="en">
<head>
<meta charset="utf-8">
<title>Vanilla Options – Two Page Flyer</title>
<link rel="stylesheet" href="https://fonts.googleapis.com/css2?family=Roboto:ital,wght@0,400;0,500;0,700;1,400;1,700&display=swap">
<style>
:root{
  --bg:#e3e3e5;
  --paper:#fafafc;
  --blue:#1f77c6;
  --blue-dark:#1a68b0;
  --teal:#3fcfb9;
  --tan:#d5c393;
  --indigo:#5b50d8;
  --red:#d14b4b;
  --navy:#38365f;
  --grey:#9a9a9a;
  --ink:#333;
  --icon-grey:#a3a3a6;
}
*{box-sizing:border-box;margin:0;padding:0}
html,body{width:1200px;height:1200px;overflow:hidden}
body{background:var(--bg);font-family:"Roboto",sans-serif;color:var(--ink);position:relative}
.page{position:absolute;top:248px;width:502px;height:704px;background:var(--paper);overflow:hidden}
.page--front{left:55px}
.page--back{left:643px}
.abs{position:absolute}
.photo{position:absolute}
.stripe{position:absolute;left:0;right:0;height:6px;display:flex}
.stripe span{flex:1}
.c1{background:var(--tan)}.c2{background:var(--teal)}.c3{background:var(--indigo)}.c4{background:var(--red)}.c5{background:var(--navy)}
.brand{position:absolute;font-family:"Roboto",sans-serif;font-weight:500;color:var(--blue);line-height:1;letter-spacing:.5px}
.body{font-size:7px;line-height:8.9px;text-align:justify;color:var(--ink)}
.body p+p{margin-top:8px}
h2.title{font-weight:500;color:var(--blue-dark);font-size:18.5px;line-height:22px}
h3.sub{font-weight:400;color:var(--blue-dark);font-size:12.5px;line-height:15px}
.checks{list-style:none;font-size:7px;line-height:13px}
.checks li{padding-left:11px;position:relative}
.checks li::before{content:"";position:absolute;left:1px;top:3.5px;width:5px;height:2.5px;border-left:1.2px solid #222;border-bottom:1.2px solid #222;transform:rotate(-45deg)}
.bullets{list-style:none;font-size:7px;line-height:8.6px}
.bullets li{padding-left:12px;position:relative;margin-bottom:4.6px}
.bullets li::before{content:"";position:absolute;left:1px;top:1.5px;width:5.5px;height:5.5px;border-radius:50%;background:#222;box-shadow:inset 0 0 0 1.6px #222}
.bullets li::after{content:"";position:absolute;left:3.2px;top:3.7px;width:1.2px;height:1.2px;background:#fff;border-radius:50%}
.footer{position:absolute;left:21px;width:463px;top:658px;height:27px;display:flex;color:#fff;font-weight:500;font-size:12.5px}
.footer .tag{width:137px;background:var(--blue);display:flex;align-items:center;justify-content:center}
.footer .line{flex:1;background:var(--grey);display:flex;align-items:center;justify-content:center}
.section-head{position:absolute;left:21px;width:240px;height:46px}
.section-head .label{position:absolute;left:58px;top:11px;color:#fff;font-weight:500;font-size:17.5px}
.factors{list-style:none;font-size:7px;line-height:8.6px}
.factors li{position:relative;padding-left:16px;margin-bottom:5px}
.factors li .dot{position:absolute;left:0;top:0;width:12px;height:12px;border-radius:50%;background:#1d1d1d}
.factors b{font-style:italic;font-weight:700}
</style>
</head>
<body>

<!-- Page one -->
<section class="page page--front">
  <div class="photo" role="img" aria-label="Business team meeting around a boardroom table in a bright glass office" style="left:0;top:0;width:502px;height:266px;background:linear-gradient(135deg,#c9d3db 0%,#9aa8b4 40%,#5a6570 75%,#3a424b 100%)"></div>
  <div class="abs" style="left:289px;top:16px;width:213px;height:96px;background:rgba(250,250,252,.9)"></div>
  <div class="brand" style="left:322px;top:48px;font-size:25px">Harbourline FX</div>
  <div class="stripe" style="top:280px"><span class="c1"></span><span class="c2"></span><span class="c3"></span><span class="c4"></span><span class="c5"></span><span class="c1"></span><span class="c2"></span><span class="c3"></span><span class="c4"></span><span class="c5"></span></div>

  <div class="abs" style="left:21px;top:305px;width:264px">
    <h2 class="title">How does a Vanilla Option<br>contract work?</h2>
    <div class="body" style="margin-top:9px">
      <p>The buyer of a vanilla option receives protection against an adverse movement in the exchange rate while allowing full participation in a beneficial move. At no time is the buyer of a Vanilla Option obligated to exercise the Option and transact the currencies, therefore providing flexibility in cases where the requirement to purchase foreign currency is not certain.</p>
      <p style="margin-top:12px">A buyer of vanilla options is required to pay a premium (like an insurance premium) for the right, but not the obligation, to exchange currency at a predetermined rate on a predetermined date.</p>
    </div>
    <ul class="checks" style="margin-top:9px">
      <li>Set a protection rate which will be your worst-case scenario at expiry</li>
      <li>Determine the amount of currency you wish to protect</li>
      <li>Choose an expiry date for the contract</li>
      <li>Calculate the premium you are required to pay</li>
    </ul>
    <h3 class="sub" style="margin-top:8px">Let’s look at an example: You are in importer.</h3>
    <div class="body" style="margin-top:10px">
      <p>Your construction company has bid on a project that if successful, will require you to import materials from the United States to use in construction. You have used todays pricing of materials in calculating your bid and want to protect against an adverse move in the US dollar exchange rate from eroding your margin if your bid is chosen for the project.</p>
      <p style="margin-top:12px">You choose to buy a Vanilla Call which will protect you from a rise in the USD/CAD exchange rate above your protection rate. You choose to buy protection on $500,000 USD, with a protection rate (strike rate) of 1.3300 expiring 3 months from now. You are required to pay a premium which in this case is calculated to be 1.8%, or 11,970 CAD.</p>
    </div>
  </div>

  <div class="abs" style="left:302px;top:308px;width:183px">
    <div class="body"><p>Your bid is successful: If the exchange rate is below your protection rate at expiration, you have no obligation relating to the vanilla call and you are free to buy USD at the cheaper spot rate. If the exchange rate is above your protection rate, your have the right to purchase your USD at the protection rate, and thereby claiming your insurance policy.</p></div>
  </div>
  <div class="photo" role="img" aria-label="Presenter at a whiteboard addressing colleagues seated at a conference table" style="left:302px;top:390px;width:183px;height:128px;background:linear-gradient(160deg,#d5dbe0 0%,#a9b3bb 45%,#4d5761 100%)"></div>
  <div class="abs" style="left:302px;top:541px;width:183px">
    <div class="body"><p>Your bid is not successful: You have no obligation relating to the vanilla option however, if at expiry the exchange rate is above the protection rate, you may exercise your right to buy USD at the lower rate and simultaneous sell USD back at the prevailing spot rate, thereby recouping some or all of the premium paid to buy the option. Alternatively, if you find out your bid was not successful with time still left until expiration, you may sell your option back into the market in the case that it still has residual value, which will depend on various market factors.</p></div>
  </div>

  <div class="footer"><div class="tag">Lorem Ipsum</div><div class="line">Lorem Ipsum is simply dummy text</div></div>
</section>

<!-- Page two -->
<section class="page page--back">
  <div class="photo" role="img" aria-label="Smiling group of young colleagues gathered around a laptop" style="left:186px;top:0;width:316px;height:144px;background:linear-gradient(100deg,#f2f2f4 0%,#c9b8a8 30%,#8d7a6c 60%,#d8dde3 100%)"></div>
  <div class="brand" style="left:36px;top:68px;font-size:25px">Harbourline FX</div>
  <div class="stripe" style="top:154px"><span class="c1"></span><span class="c2"></span><span class="c3"></span><span class="c4"></span><span class="c5"></span><span class="c1"></span><span class="c2"></span><span class="c3"></span><span class="c4"></span><span class="c5"></span></div>

  <!-- Characteristics -->
  <div class="section-head" style="top:191px">
    <svg width="240" height="46" viewBox="0 0 240 46">
      <polygon points="40,4 216,4 205,38 40,38" fill="var(--blue)"/>
      <polygon points="216,4 221,4 210,38 205,38" fill="var(--teal)"/>
      <circle cx="23" cy="23" r="22" fill="#d6d6d8"/>
      <circle cx="23" cy="23" r="19" fill="var(--icon-grey)"/>
      <g fill="none" stroke="#fff" stroke-width="1.2">
        <polygon points="23,13 31,17.5 31,27.5 23,32 15,27.5 15,17.5"/>
        <polyline points="15,17.5 23,22 31,17.5"/><line x1="23" y1="22" x2="23" y2="32"/>
      </g>
    </svg>
    <div class="label">Characteristics</div>
  </div>
  <ul class="bullets abs" style="left:21px;top:248px;width:266px">
    <li>You are looking for a straight-forward hedging solution</li>
    <li>You want to receive full benefit from an appreciation of the currency you are exposed to</li>
    <li>You are comfortable receiving protection at the strike rate of the option</li>
    <li>You are willing to pay the non-refundable premium</li>
  </ul>

  <!-- Advantages -->
  <div class="section-head" style="top:326px">
    <svg width="240" height="46" viewBox="0 0 240 46">
      <polygon points="40,4 216,4 205,38 40,38" fill="var(--blue)"/>
      <polygon points="216,4 221,4 210,38 205,38" fill="var(--teal)"/>
      <circle cx="23" cy="23" r="22" fill="#d6d6d8"/>
      <circle cx="23" cy="23" r="19" fill="var(--icon-grey)"/>
      <g fill="#fff"><rect x="19.5" y="20" width="7" height="11"/><rect x="13" y="24" width="6" height="7"/><rect x="27" y="25.5" width="6" height="5.5"/><circle cx="23" cy="15" r="2"/></g>
    </svg>
    <div class="label">Advantages</div>
  </div>
  <ul class="bullets abs" style="left:21px;top:382px;width:266px">
    <li>You hedge your foreign currency exposure at a predefined hedge rate</li>
    <li>You can choose the hedge rate that suits your budget requirements</li>
    <li>Provides the ability to fully participate in a favourable exchange rate move</li>
    <li>You can choose from most major currency pairs to meet your needs</li>
  </ul>

  <!-- Risks -->
  <div class="section-head" style="top:449px">
    <svg width="240" height="46" viewBox="0 0 240 46">
      <polygon points="40,4 216,4 205,38 40,38" fill="var(--blue)"/>
      <polygon points="216,4 221,4 210,38 205,38" fill="var(--teal)"/>
      <circle cx="23" cy="23" r="22" fill="#d6d6d8"/>
      <circle cx="23" cy="23" r="19" fill="var(--icon-grey)"/>
      <polygon points="23,12 34,31 12,31" fill="none" stroke="#fff" stroke-width="1.6" stroke-linejoin="round"/>
      <rect x="22.2" y="18" width="1.6" height="7.5" fill="#fff"/><circle cx="23" cy="28" r="1" fill="#fff"/>
    </svg>
    <div class="label">Risks</div>
  </div>
  <ul class="bullets abs" style="left:21px;top:508px;width:266px">
    <li>Premium paid is non-refundable and remains your only obligation when buying vanilla options</li>
  </ul>
  <div class="photo" role="img" aria-label="Two business people shaking hands against a sunlit window" style="left:35px;top:540px;width:224px;height:108px;background:linear-gradient(120deg,#2b3a58 0%,#3e4f6e 40%,#c9cfd6 70%,#5d6b6f 100%)"></div>

  <!-- Right column -->
  <div class="abs" style="left:298px;top:191px;width:184px">
    <h3 class="sub">Why use Vanilla Options?</h3>
    <div class="body" style="margin-top:6px"><p>Vanilla options are often compared to an insurance product. The buyer pays a non-refundable premium for the right, but not the obligation to trade currency in the future at the protection rate of the option. This product allows you to participate in a beneficial move to an unlimited extent, which will be the most advantageous outcome, if the exchange rate moves in your favour enough to more than offset the premium paid for the option.</p></div>
    <h3 class="sub" style="margin-top:16px">What determines the price of a Vanilla Option?</h3>
    <div class="body" style="margin-top:9px"><p>The cost of an option is defined by the premium that is required to be paid in order to enter into the contract. Premiums are calculated using the industry standard formulas based upon the Black Scholes model. The most important variables in the option pricing formulas include the following:</p></div>
    <ul class="factors" style="margin-top:12px">
      <li>The current market Spot Rate.</li>
      <li><span class="dot"></span><b>Market volatility</b> – the higher the volatility, the higher the premium.</li>
      <li><span class="dot"></span><b>The Term of the Option</b> – a longer term typically results in a higher premium.</li>
      <li><span class="dot"></span><b>The Strike Rate</b> – the closer to being ITM the protection rate is, the higher the premium.</li>
      <li>The interest rate differential of the two currencies involved.</li>
      <li><span class="dot"></span><b>Style</b> – European or American, or whether the option can be exercised prior to expiration</li>
    </ul>
    <div class="body" style="margin-top:10px"><p>An option can either a European (meaning that they can only be exercised on the expiry date), or American (meaning that they can be exercised at any time prior to expiration). We normally deals in European options however, we do offer American options under certain circumstances and when specific delivery terms are agreed upon between us and the customer.</p></div>
  </div>

  <div class="footer"><div class="tag">Lorem Ipsum</div><div class="line">Lorem Ipsum is simply dummy text</div></div>
</section>

</body>
</html>
```